Looking for a "Hipster orientated" menu design for our espresso bar.
Lantern Brewhouse is part of the Marlow Kettle Group a leading Australian roasting company.
We are leaving the brief open as we don't to use any pre-conceived ideas that are in our heads. In a nutshell we don't want to be an imitation of others.
Lantern Brewhouse is an industrial inspired space with some classic elements. Coffee is our passion and simple fresh well presented food to match using the best local ingredients.

We would like our menu to have a clear distinction between beverages and food.
An open A4 size menu landscape format is ideal or perhaps folded.

This is our first crowd sourced design and the menu is a test to what will be a new webpage, online store and new brand elements for our company to the right designer.

At this stage don't worry about content i.e whats in a sandwich. Random latin under the word breakfast burger is fine.

Good luck

Target Market(s)

Hipster caffeine and food addicts

Industry/Entity Type

Industrial

Font styles to use
Decorative

Colors

Designer to choose colors to be used in the design.

Requirements
Must have
• A distinction between breakfast, lunch and beverages/coffee
Should not have
• overcrowded, hard to read

```html
<!DOCTYPE html>
<html lang="en">
<head>
<meta charset="utf-8">
<title>Lantern Brewhouse Menu</title>
<link rel="stylesheet" href="https://fonts.googleapis.com/css2?family=Cinzel:wght@700&family=Lobster+Two:ital,wght@1,700&family=Montserrat:wght@700&family=Varela+Round&display=swap">
<style>
  :root {
    --paper: #e8894a;
    --paper-deep: #df7d3e;
    --panel: rgba(250, 214, 186, 0.72);
    --ink: #3c3c3e;
    --ink-soft: #4a4a4c;
    --title: #ececec;
    --ornament: rgba(60, 60, 62, 0.22);
    --ornament-faint: rgba(60, 60, 62, 0.16);
  }
  * { margin: 0; padding: 0; box-sizing: border-box; }
  html, body { width: 1200px; height: 849px; overflow: hidden; }
  body {
    position: relative;
    background: linear-gradient(180deg, var(--paper) 0%, var(--paper-deep) 100%);
    color: var(--ink);
    font-family: "Varela Round", sans-serif;
  }
  .panel {
    position: absolute;
    background: var(--panel);
    border-radius: 14px;
    text-align: center;
  }
  .panel--drinks { left: 78px; top: 122px; width: 358px; height: 578px; }
  .panel--food { left: 600px; top: 26px; width: 568px; height: 800px; }

  .heading {
    font-family: "Lobster Two", cursive;
    font-style: italic;
    font-weight: 700;
    color: var(--ink);
    line-height: 1;
  }
  .price {
    font-family: "Montserrat", sans-serif;
    font-weight: 700;
    letter-spacing: 1px;
    color: var(--ink);
  }
  .ornament {
    display: block;
    margin: 0 auto;
    border-radius: 10px;
    background: var(--ornament);
  }

  /* Beverages */
  .drink { position: absolute; left: 0; width: 100%; }
  .drink .heading { font-size: 25px; }
  .drink p { font-size: 16.5px; color: var(--ink-soft); line-height: 21px; margin-top: 2px; }
  .drink .price { font-size: 13px; margin-top: 3px; }
  .drink .ornament { width: 42px; height: 10px; margin-top: 22px; background: var(--ornament-faint); }
  .flourish {
    position: absolute; left: 162px; width: 194px; height: 44px;
    border-radius: 22px; background: var(--ornament);
  }

  /* Title column */
  .title-rule { position: absolute; top: 12px; width: 1px; height: 822px; background: var(--title); opacity: 0.8; }
  .brand {
    position: absolute;
    left: 100px; top: 394px;
    width: 820px; height: 60px;
    transform: rotate(-90deg);
    text-align: center;
    white-space: nowrap;
    font-family: "Cinzel", serif;
    font-weight: 700;
    font-size: 50px;
    line-height: 60px;
    letter-spacing: 5px;
    color: var(--title);
  }
  .brand .initial { font-size: 66px; }

  /* Food */
  .section-title { position: absolute; left: 0; width: 100%; display: flex; justify-content: center; align-items: center; gap: 10px; }
  .section-title .heading { font-size: 23px; }
  .section-title .ornament { width: 42px; height: 12px; margin: 0; }
  .dish-list { position: absolute; left: 0; width: 100%; list-style: none; }
  .dish { height: 39px; }
  .dish p { font-size: 12.5px; line-height: 15px; color: var(--ink-soft); }
  .dish .price { font-size: 10px; line-height: 14px; }
  .divider { position: absolute; left: 232px; width: 112px; height: 26px; border-radius: 13px; background: var(--ornament); }
  .sub-col { position: absolute; width: 260px; text-align: center; }
  .sub-col .heading { font-size: 16px; display: block; margin-bottom: 12px; }
  .sub-col .dish-list { position: static; }
</style>
</head>
<body>

  <span class="flourish" style="top:52px" role="img" aria-label="Decorative swirl flourish"></span>

  <section class="panel panel--drinks" aria-label="Beverages">
    <div class="drink" style="top:15px">
      <h2 class="heading">Coffee</h2>
      <p>Rior assin escilique se veribus tisquiae.</p>
      <div class="price">$3.50</div>
      <span class="ornament" role="img" aria-label="Small swirl divider"></span>
    </div>
    <div class="drink" style="top:132px">
      <h2 class="heading">Traditional Espresso</h2>
      <p>Rior assin escilique se veribus tisquiae.</p>
      <div class="price">$3.50</div>
      <span class="ornament" role="img" aria-label="Small swirl divider"></span>
    </div>
    <div class="drink" style="top:249px">
      <h2 class="heading">Blended Drinks</h2>
      <p>Ehent, qui quam re latur tisquiae.</p>
      <div class="price">$3.50</div>
      <span class="ornament" role="img" aria-label="Small swirl divider"></span>
    </div>
    <div class="drink" style="top:365px">
      <h2 class="heading">Tea</h2>
      <p>Nem elendi ipitate plabo.</p>
      <div class="price">$3.50</div>
      <span class="ornament" role="img" aria-label="Small swirl divider"></span>
    </div>
    <div class="drink" style="top:481px">
      <h2 class="heading">Other Drinks</h2>
      <p>Videm rem ilibeatem<br>ipsam que quibus dolorpo.</p>
      <div class="price">$3.50</div>
    </div>
  </section>

  <span class="flourish" style="top:728px" role="img" aria-label="Decorative swirl flourish"></span>

  <span class="title-rule" style="left:483px"></span>
  <span class="title-rule" style="left:537px"></span>
  <h1 class="brand"><span class="initial">L</span>ANTERN <span class="initial">B</span>REWHOUSE</h1>

  <section class="panel panel--food" aria-label="Food">
    <div class="section-title" style="top:11px">
      <span class="ornament" role="img" aria-label="Small swirl"></span>
      <h2 class="heading">Breakfast</h2>
      <span class="ornament" role="img" aria-label="Small swirl"></span>
    </div>
    <ul class="dish-list" style="top:47px">
      <li class="dish"><p>Rior assin escilique se veribus tisquiae.</p><div class="price">$5.50</div></li>
      <li class="dish"><p>Rior assin escilique se veribus tisquiae.</p><div class="price">$5.50</div></li>
      <li class="dish"><p>Rior assin escilique se veribus tisquiae.</p><div class="price">$5.50</div></li>
      <li class="dish"><p>Rior assin escilique se veribus tisquiae.</p><div class="price">$5.50</div></li>
      <li class="dish"><p>Rior assin escilique se veribus tisquiae.</p><div class="price">$5.50</div></li>
    </ul>

    <span class="divider" style="top:236px" role="img" aria-label="Swirl divider"></span>

    <div class="section-title" style="top:272px">
      <h2 class="heading">Lunch</h2>
    </div>
    <ul class="dish-list" style="top:307px">
      <li class="dish"><p>Rior assin escilique se veribus tisquiae.</p><div class="price">$8.50</div></li>
      <li class="dish"><p>Rior assin escilique se veribus tisquiae.</p><div class="price">$8.50</div></li>
      <li class="dish"><p>Rior assin escilique se veribus tisquiae.</p><div class="price">$8.50</div></li>
      <li class="dish"><p>Rior assin escilique se veribus tisquiae.</p><div class="price">$8.50</div></li>
      <li class="dish"><p>Rior assin escilique se veribus tisquiae.</p><div class="price">$8.50</div></li>
    </ul>

    <div class="sub-col" style="left:22px; top:512px">
      <h3 class="heading">Soup</h3>
      <ul class="dish-list">
        <li class="dish"><p>Rior assin escilique se veribus tisquiae.</p><div class="price">$4.50</div></li>
        <li class="dish"><p>Rior assin escilique se veribus tisquiae.</p><div class="price">$4.50</div></li>
      </ul>
    </div>
    <span class="ornament" style="position:absolute; left:264px; top:512px; width:50px; height:14px" role="img" aria-label="Small swirl"></span>
    <div class="sub-col" style="left:300px; top:512px">
      <h3 class="heading">Salad</h3>
      <ul class="dish-list">
        <li class="dish"><p>Rior assin escilique se veribus tisquiae.</p><div class="price">$4.50</div></li>
        <li class="dish"><p>Rior assin escilique se veribus tisquiae.</p><div class="price">$4.50</div></li>
      </ul>
    </div>

    <span class="divider" style="top:608px" role="img" aria-label="Swirl divider"></span>

    <div class="section-title" style="top:648px">
      <h2 class="heading">Desserts</h2>
    </div>
    <ul class="dish-list" style="top:683px">
      <li class="dish"><p>Rior assin escilique se veribus tisquiae.</p><div class="price">$4.00</div></li>
      <li class="dish"><p>Rior assin escilique se veribus tisquiae.</p><div class="price">$4.00</div></li>
      <li class="dish"><p>Rior assin escilique se veribus tisquiae.</p><div class="price">$4.00</div></li>
    </ul>
  </section>

</body>
</html>
```